Street Light Box

We need a New Illuminated light Box Sign. See size in attached document and pics of current sign.
The light box needs to contain "The Harbourview Motel"and then in one third of the box at the bottom promote the restaurant on site. I want white text on black without the logo. Harbourview to be prominent word with elongated text to maximise text size for maximum visibility from a distance.

Target Market(s)

Catch attention of motel

Industry/Entity Type

Motel accommodation

Logo Text

The Harbourview Motel and below Morikawa Grillhouse Restaurant

Logo styles of interest
Wordmark Logo
Lettermark Logo
Font styles to use
Sans Serif

Colors

Designer to choose only greyscale colors for use in the design.

Requirements
Must have
• Fit in Light Box
Nice to have
• Make Harbourview the Champion work with Elongated thick Text

```html
<!DOCTYPE html>
<html lang="en">
<head>
<meta charset="utf-8">
<title>The Harbourview Motel – Light Box Sign</title>
<link rel="stylesheet" href="https://fonts.googleapis.com/css2?family=Montserrat:wght@700;800&family=Oswald:wght@600&display=swap">
<style>
  :root {
    --backdrop: #3b3a3c;
    --sign-grey: #6e6e6e;
    --band-black: #000000;
    --panel-white: #ffffff;
    --ink-black: #111111;
  }
  * { margin: 0; padding: 0; box-sizing: border-box; }
  html, body {
    width: 961px;
    height: 1200px;
    overflow: hidden;
    background: var(--backdrop);
  }
  .canvas {
    position: relative;
    width: 961px;
    height: 1200px;
  }
  .light-box {
    position: absolute;
    left: 214px;
    top: 334px;
    width: 534px;
    height: 533px;
    background: var(--panel-white);
    overflow: hidden;
  }
  .motel-panel {
    position: absolute;
    left: 0; top: 0;
    width: 100%;
    height: 320px;
    background: var(--sign-grey);
  }
  .motel-article {
    position: absolute;
    left: 0; right: 0;
    top: 72px;
    text-align: center;
    font-family: "Montserrat", sans-serif;
    font-weight: 800;
    font-size: 29px;
    line-height: 36px;
    color: var(--panel-white);
    letter-spacing: 1px;
  }
  .name-band {
    position: absolute;
    left: 0; top: 120px;
    width: 100%;
    height: 97px;
    background: var(--band-black);
    display: flex;
    align-items: center;
    justify-content: center;
  }
  .motel-name {
    font-family: "Montserrat", sans-serif;
    font-weight: 800;
    font-size: 57px;
    line-height: 1;
    color: var(--panel-white);
    letter-spacing: 1px;
    white-space: nowrap;
  }
  .motel-word-row {
    position: absolute;
    left: 0; top: 228px;
    width: 100%;
    height: 54px;
    display: flex;
    align-items: center;
  }
  .rule {
    flex: 1;
    height: 4px;
    background: var(--panel-white);
  }
  .motel-word {
    padding: 0 20px;
    font-family: "Montserrat", sans-serif;
    font-weight: 800;
    font-size: 51px;
    line-height: 54px;
    color: var(--panel-white);
    letter-spacing: 1px;
  }
  .restaurant-panel {
    position: absolute;
    left: 0; top: 320px;
    width: 100%;
    height: 213px;
    display: flex;
    flex-direction: column;
    align-items: center;
    justify-content: center;
  }
  .restaurant-lockup {
    display: flex;
    flex-direction: column;
    align-items: flex-end;
  }
  .restaurant-name {
    font-family: "Montserrat", sans-serif;
    font-weight: 800;
    font-size: 62px;
    line-height: 64px;
    color: var(--ink-black);
  }
  .restaurant-type {
    margin-top: 2px;
    font-family: "Oswald", sans-serif;
    font-weight: 600;
    font-size: 26px;
    line-height: 30px;
    color: var(--ink-black);
  }
</style>
</head>
<body>
  <main class="canvas">
    <section class="light-box" aria-label="The Harbourview Motel street light box sign">
      <div class="motel-panel">
        <p class="motel-article">THE</p>
        <div class="name-band">
          <h1 class="motel-name">HARBOURVIEW</h1>
        </div>
        <div class="motel-word-row">
          <span class="rule"></span>
          <span class="motel-word">MOTEL</span>
          <span class="rule"></span>
        </div>
      </div>
      <div class="restaurant-panel">
        <div class="restaurant-lockup">
          <p class="restaurant-name">Morikawa</p>
          <p class="restaurant-type">Grillhouse Restaurant</p>
        </div>
      </div>
    </section>
  </main>
</body>
</html>
```